Tradeplazas Orbit

The Business card will a 2 sided.
1) Front Side you will use logo1.png the other details will be
Gerald Pattersonby
CTO
Trade Plazas Orbit

+61 407 362 518
gerald@tradeplazasorbit-example.com
www.tradeplazasorbit-example.com

2) Reverse side, needs to have all logo's 2,3,4,5,6,7 . png

the rest of the design is up to you

```html
<!DOCTYPE html>
<html lang="en">
<head>
<meta charset="utf-8">
<title>Trade Plazas Orbit – Business Card</title>
<link href="https://fonts.googleapis.com/css2?family=Arimo:wght@400;700&family=Russo+One&display=swap" rel="stylesheet">
<style>
  :root {
    --ink: #0a1520;
    --cyan: #00f6fb;
    --panel: #e6e6e6;
    --white: #ffffff;
    --line: #1a1a1a;
    --mark: #4a5560;
  }
  * { box-sizing: border-box; margin: 0; padding: 0; }
  html, body { width: 986px; height: 1200px; overflow: hidden; background: var(--white); }
  body { position: relative; font-family: "Arimo", Arial, sans-serif; }
  .sheet-frame { position: absolute; left: 1px; top: 1px; width: 984px; height: 1198px; border: 1.5px solid var(--line); }
  .abs { position: absolute; }

  /* front */
  .front { left: 71px; top: 50px; width: 866px; height: 530px; }
  .front-logo-panel { left: 0; top: 0; width: 359px; height: 530px; background: var(--panel); border: 1px solid #c8c8c8; }
  .front-contact-panel { left: 359px; top: 0; width: 507px; height: 530px; background: var(--ink); }
  .brand-lockup { left: 0; top: 150px; width: 359px; display: flex; flex-direction: column; align-items: center; gap: 14px; }
  .brand-dot { width: 42px; height: 42px; border-radius: 50%; background: var(--mark); }
  .brand-name { font-weight: 700; font-size: 26px; color: var(--mark); text-align: center; line-height: 1.2; }

  .contact-row { left: 404px; display: flex; align-items: center; gap: 16px; color: var(--white); font-size: 23px; }
  .contact-row svg { width: 54px; height: 54px; flex: none; }

  .title-band { left: 0; top: 382px; width: 358px; height: 93px; background: var(--white); border-top: 4px solid var(--cyan); border-bottom: 4px solid var(--cyan); padding: 16px 0 0 71px; font-size: 23px; line-height: 28px; color: #111; }
  .name-band { left: 357px; top: 382px; width: 509px; height: 93px; background: var(--cyan); border-top: 3px solid var(--white); border-bottom: 3px solid var(--white); display: flex; align-items: center; padding-left: 30px; }
  .person-name { font-family: "Russo One", "Arimo", sans-serif; font-size: 39px; color: var(--white); letter-spacing: 0.5px; }

  /* back */
  .back { left: 75px; top: 623px; width: 865px; height: 529px; background: var(--panel); overflow: hidden; }
  .region-mark { width: 170px; display: flex; flex-direction: column; align-items: center; gap: 10px; }
  .region-square { width: 22px; height: 16px; background: var(--mark); }
  .region-name { font-weight: 700; font-size: 20px; color: var(--mark); text-align: center; line-height: 1.2; }
  .footer-dark { left: 0; top: 460px; width: 865px; height: 69px; background: var(--ink); }
  .footer-cyan { top: 443px; height: 38px; background: var(--cyan); }
  .footer-url { left: 281px; top: 443px; width: 300px; height: 17px; text-align: center; font-size: 16px; color: #111; line-height: 17px; background: var(--panel); }
</style>
</head>
<body>
<div class="sheet-frame"></div>

<section class="abs front" aria-label="Card front">
  <div class="abs front-logo-panel"></div>
  <div class="abs front-contact-panel"></div>

  <div class="abs brand-lockup">
    <div class="brand-dot"></div>
    <div class="brand-name">Trade Plazas Orbit</div>
  </div>

  <div class="abs contact-row" style="top:80px">
    <svg viewBox="0 0 54 54" aria-hidden="true"><circle cx="27" cy="27" r="25" fill="none" stroke="#fff" stroke-width="3"/><path d="M18 14c2-2 4-1 5 1l3 5c1 2 0 3-1 4l-2 2c1 3 4 6 7 7l2-2c1-1 2-2 4-1l5 3c2 1 3 3 1 5-3 3-7 4-12 1-6-4-10-9-13-14-2-5-2-8 1-11z" fill="#fff"/></svg>
    <span>+61 407 362 518</span>
  </div>
  <div class="abs contact-row" style="top:155px">
    <svg viewBox="0 0 54 54" aria-hidden="true"><circle cx="27" cy="27" r="25" fill="none" stroke="#fff" stroke-width="3"/><rect x="13" y="18" width="28" height="19" fill="#fff"/><path d="M13 18l14 11 14-11" fill="none" stroke="#0a1520" stroke-width="2"/></svg>
    <span>gerald@tradeplazasorbit-example.com</span>
  </div>
  <div class="abs contact-row" style="top:230px">
    <svg viewBox="0 0 54 54" aria-hidden="true"><g fill="none" stroke="#fff" stroke-width="3"><circle cx="27" cy="27" r="24"/><ellipse cx="27" cy="27" rx="10" ry="24"/><line x1="27" y1="3" x2="27" y2="51"/><line x1="3" y1="27" x2="51" y2="27"/><path d="M7 15h40M7 39h40"/></g></svg>
    <span>www.tradeplazasorbit-example.com</span>
  </div>

  <div class="abs title-band">CTO<br>Trade Plazas Orbit</div>
  <div class="abs name-band"><span class="person-name">Gerald Pattersonby</span></div>
</section>

<section class="abs back" aria-label="Card back">
  <div class="abs region-mark" style="left:107px;top:95px"><div class="region-square"></div><div class="region-name">Trade Plazas Orbit<br>Australia</div></div>
  <div class="abs region-mark" style="left:348px;top:95px"><div class="region-square"></div><div class="region-name">Trade Plazas Orbit<br>USA</div></div>
  <div class="abs region-mark" style="left:586px;top:95px"><div class="region-square"></div><div class="region-name">Trade Plazas Orbit<br>UK</div></div>
  <div class="abs region-mark" style="left:107px;top:295px"><div class="region-square"></div><div class="region-name">Trade Plazas Orbit<br>Asia</div></div>
  <div class="abs region-mark" style="left:348px;top:295px"><div class="region-square"></div><div class="region-name">Trade Plazas Orbit<br>China</div></div>
  <div class="abs region-mark" style="left:586px;top:295px"><div class="region-square"></div><div class="region-name">Trade Plazas Orbit<br>India</div></div>

  <div class="abs footer-dark"></div>
  <div class="abs footer-cyan" style="left:0;width:281px"></div>
  <div class="abs footer-cyan" style="left:581px;width:284px"></div>
  <div class="abs footer-url">www.tradeplazasorbit-example.com</div>
</section>
</body>
</html>
```